Brightmoor Card Company Business Cards

We are a trading card store with Zorblix, sports and other TCG cards, we need a business card design that encompasses a clean cut, modern style with a retro flare. website is brightmoorcardco.com for reference. Can utilize a comic book era feel or a more modern outdoor feel to utilize the "Pacific Northwest" elements of tress, mountains, etc.

Industry/Entity Type

Trading cards and collectibles

Contact Information for Business Card

business name, email address, phone number, name, owner job title

Font styles to use
Sans Serif

```html
<!DOCTYPE html>
<html lang="en">
<head>
<meta charset="utf-8">
<title>Brightmoor Card Company – Business Cards</title>
<link href="https://fonts.googleapis.com/css2?family=Lato:wght@400;700;900&display=swap" rel="stylesheet">
<style>
  :root {
    --backdrop: #3a3a3a;
    --card: #050505;
    --ink: #f2f2f2;
    --accent: #12b9dd;
    --rule: #d8d8d8;
    --muted: #8a8a8a;
  }
  * { margin: 0; padding: 0; box-sizing: border-box; }
  html, body {
    width: 1200px; height: 689px; overflow: hidden;
    background: var(--backdrop);
    font-family: "Lato", Arial, sans-serif;
  }
  .sheet {
    position: relative; width: 1200px; height: 689px;
    display: flex; align-items: center; justify-content: center; gap: 60px;
  }
  .card {
    position: relative;
    width: 520px; height: 298px;
    background: var(--card);
    border-radius: 18px;
    box-shadow: 0 18px 40px rgba(0,0,0,.45);
    color: var(--ink);
  }
  .brand-mark {
    display: flex; align-items: center; gap: 10px;
    color: var(--ink);
    font-weight: 900;
    text-transform: uppercase;
    letter-spacing: .06em;
    line-height: 1.1;
  }
  .brand-mark .dot {
    flex: none; border-radius: 50%; background: var(--accent);
  }
  .card-front .brand-mark {
    position: absolute; inset: 0;
    justify-content: center;
    font-size: 26px;
  }
  .card-front .brand-mark .dot { width: 22px; height: 22px; }

  .card-back .brand-mark {
    position: absolute; top: 34px; right: 34px;
    font-size: 15px;
    text-align: right;
  }
  .card-back .brand-mark .dot { width: 14px; height: 14px; }

  .rule-top {
    position: absolute; left: 34px; right: 34px; top: 112px;
    height: 1px; background: var(--rule);
  }
  .address {
    position: absolute; right: 34px; top: 126px;
    text-align: right; font-size: 13px; line-height: 1.45;
  }
  .person {
    position: absolute; left: 34px; top: 158px;
  }
  .person-name {
    color: var(--accent); font-size: 26px; font-weight: 400;
    text-transform: uppercase; letter-spacing: -.01em; line-height: 1;
  }
  .person-title { font-size: 14px; margin-top: 6px; }
  .rule-mid {
    position: absolute; left: 34px; width: 240px; top: 216px;
    height: 1px; background: var(--rule);
  }
  .contacts {
    position: absolute; left: 34px; top: 226px;
    list-style: none; font-size: 13px; line-height: 19px;
  }
  .contacts li { display: flex; align-items: center; gap: 10px; }
  .contacts svg { width: 13px; height: 13px; flex: none; }
</style>
</head>
<body>
<main class="sheet">
  <section class="card card-front" aria-label="Card front">
    <div class="brand-mark"><span class="dot"></span><span>Brightmoor<br>Card Company</span></div>
  </section>

  <section class="card card-back" aria-label="Card back">
    <div class="brand-mark"><span class="dot"></span><span>Brightmoor<br>Card Company</span></div>
    <div class="rule-top"></div>
    <p class="address">421, Address line goes here<br>45452, Country name</p>

    <div class="person">
      <h1 class="person-name">Marcus Ellery</h1>
      <p class="person-title">Managing Director</p>
    </div>
    <div class="rule-mid"></div>

    <ul class="contacts">
      <li>
        <svg viewBox="0 0 16 16" fill="none" stroke="#bdbdbd" stroke-width="1.6"><path d="M3 2h3l1.5 3.5-2 1.2a8 8 0 0 0 3.8 3.8l1.2-2L14 10v3a1 1 0 0 1-1 1A11 11 0 0 1 2 3a1 1 0 0 1 1-1z"/></svg>
        <span>044-555 218 904</span>
      </li>
      <li>
        <svg viewBox="0 0 16 16" fill="none" stroke="#bdbdbd" stroke-width="1.6"><rect x="1.5" y="3.5" width="13" height="9"/><path d="M1.5 3.5 8 9l6.5-5.5"/></svg>
        <span>hello@brightmoorcardco.com</span>
      </li>
      <li>
        <svg viewBox="0 0 16 16" fill="none" stroke="#bdbdbd" stroke-width="1.4"><circle cx="8" cy="8" r="6.5"/><ellipse cx="8" cy="8" rx="3" ry="6.5"/><path d="M1.5 8h13"/></svg>
        <span>www.brightmoorcardco.com</span>
      </li>
    </ul>
  </section>
</main>
</body>
</html>
```